WORK VAN WRAP - Granitewell Floor Coating

I need full-wrap design for my Concrete Coating Business.
Vehicle is: 2019 Vell Cargoline 3300 Hi roof cargo van
My business expertise is: Epoxy Floor Coating including Luxuxry Flakes, Luxury Metallics, and Luxury Quartz for outdoor. But the core of my business is in doing the 1-DAY GARAGE FLOOR APPLICATION.
My work is: LifetimeWarranty
My website is not active yet but it will be soon: GRANITEWELLFLOORCOATING.COM
Phone number: coming soon
Email: coming soon
Colors:
45% black
25% neon green (follow the logo attached)
20% white (for lettering)
10% gray (real picture of a floor attached) feel free about using a better picture
I will attach some pictures of designs I've seen for inspiration purposes only.
Goal: I need the vehicle to stand out among others, a bright green on black that no one can miss with an attractive design that everyone wants to know "what kind of business is that" when they see it parked or driving on the road.
Target Market(s)
USA
Industry/Entity Type
Home Improvement

```html
<!DOCTYPE html>
<html lang="en">
<head>
<meta charset="utf-8">
<title>Granitewell Floor Coatings – Van Wrap</title>
<link rel="stylesheet" href="https://fonts.googleapis.com/css2?family=Montserrat:wght@700;800&display=swap">
<style>
  :root {
    --wrap-black: #020202;
    --neon-green: #5ce000;
    --letter-white: #ffffff;
    --ink-navy: #14152a;
    --trim-gray: #3b3f48;
    --glass: #5d6168;
    --granite-light: #c9c2b6;
    --granite-dark: #9c958a;
    --page: #ffffff;
  }
  html, body {
    margin: 0;
    padding: 0;
    width: 1200px;
    height: 1103px;
    overflow: hidden;
    background: var(--page);
  }
  .wrap-sheet { display: block; width: 1200px; height: 1103px; }
  .van-body { fill: var(--wrap-black); }
  .van-trim { fill: var(--trim-gray); }
  .van-glass { fill: var(--glass); }
  .van-wheel { fill: #1c1f26; }
  .van-hub { fill: #3a3e46; }
  .accent-band { fill: var(--neon-green); }
  .accent-curve { fill: none; stroke: var(--neon-green); stroke-width: 26; }
  .brand-square { fill: none; stroke: var(--neon-green); stroke-width: 30; }
  .brand-name {
    font-family: "Montserrat", sans-serif;
    font-weight: 800;
    fill: var(--letter-white);
  }
  .brand-tagline {
    font-family: "Montserrat", sans-serif;
    font-weight: 800;
    fill: var(--neon-green);
  }
  .contact-line {
    font-family: "Montserrat", sans-serif;
    font-weight: 800;
    fill: var(--ink-navy);
  }
  .contact-icon { fill: none; stroke: var(--ink-navy); stroke-width: 7; stroke-linecap: round; stroke-linejoin: round; }
</style>
</head>
<body>
<svg class="wrap-sheet" viewBox="0 0 2000 1838" xmlns="http://www.w3.org/2000/svg">
  <defs>
    <linearGradient id="granite-tone" x1="0" y1="0" x2="1" y2="1">
      <stop offset="0" stop-color="var(--granite-light)"/>
      <stop offset="0.6" stop-color="var(--granite-dark)"/>
      <stop offset="1" stop-color="var(--granite-light)"/>
    </linearGradient>
    <clipPath id="van-outline">
      <path d="M80,72 L1280,72 Q1400,72 1450,160 L1680,370 Q1880,440 1900,540 L1945,600 L1945,760 L50,760 L50,600 L60,120 Q62,72 80,72Z"/>
    </clipPath>
    <g id="van-shell">
      <path class="van-body" d="M80,72 L1280,72 Q1400,72 1450,160 L1680,370 Q1880,440 1900,540 L1945,600 L1945,760 L50,760 L50,600 L60,120 Q62,72 80,72Z"/>
      <g clip-path="url(#van-outline)">
        <path role="img" aria-label="Granite flake floor coating texture" fill="url(#granite-tone)" d="M480,60 Q560,180 720,205 L1700,395 L1760,60Z"/>
        <path class="accent-curve" d="M470,60 Q560,185 720,208 L1700,398"/>
        <path class="accent-band" d="M60,440 L1510,640 L1460,715 L60,525Z"/>
      </g>
      <path class="van-glass" d="M1330,240 L1455,240 L1590,350 L1560,460 L1345,450 Q1325,350 1330,240Z"/>
      <path class="van-trim" d="M50,600 L270,600 Q300,590 330,590 L480,590 Q520,610 525,660 L525,765 L50,765Z"/>
      <path class="van-trim" d="M1490,760 L1500,640 Q1540,560 1640,550 L1760,550 Q1800,570 1945,600 L1945,760Z"/>
      <circle class="van-wheel" cx="368" cy="755" r="110"/>
      <circle class="van-hub" cx="368" cy="755" r="72"/>
      <circle class="van-wheel" cx="1685" cy="755" r="110"/>
      <circle class="van-hub" cx="1685" cy="755" r="72"/>
    </g>
    <g id="phone-icon">
      <path class="contact-icon" d="M0,-38 q0,34 34,34 l8,-11 l-11,-11 l-9,7 q-11,-7 -15,-15 l7,-9 l-11,-11z"/>
    </g>
    <g id="laptop-icon">
      <rect class="contact-icon" x="6" y="-40" width="34" height="26"/>
      <path class="contact-icon" d="M0,-6 h46"/>
    </g>
  </defs>

  <!-- Passenger side van -->
  <use href="#van-shell"/>
  <!-- Driver side van -->
  <use href="#van-shell" transform="translate(2000,890) scale(-1,1)"/>

  <!-- Lettering: passenger side -->
  <g class="wrap-lettering" transform="translate(400,330) rotate(8)">
    <rect class="brand-square" x="-240" y="-170" width="180" height="180"/>
    <text class="brand-name" x="0" y="0" font-size="132" textLength="820" lengthAdjust="spacingAndGlyphs">GRANITEWELL</text>
    <text class="brand-tagline" x="-7" y="95" font-size="92" textLength="810" lengthAdjust="spacingAndGlyphs">FLOOR COATINGS</text>
    <g class="contact-row" transform="translate(-255,205)">
      <use href="#phone-icon"/>
      <text class="contact-line" x="58" y="0" font-size="58" textLength="360" lengthAdjust="spacingAndGlyphs">555-014-2870</text>
      <use href="#laptop-icon" x="440"/>
      <text class="contact-line" x="505" y="0" font-size="58" textLength="570" lengthAdjust="spacingAndGlyphs">www.granitewellfloors.com</text>
    </g>
  </g>

  <!-- Lettering: driver side -->
  <g class="wrap-lettering" transform="translate(790,1335) rotate(-8)">
    <rect class="brand-square" x="885" y="-190" width="180" height="180"/>
    <text class="brand-name" x="0" y="0" font-size="130" textLength="810" lengthAdjust="spacingAndGlyphs">GRANITEWELL</text>
    <text class="brand-tagline" x="0" y="105" font-size="90" textLength="800" lengthAdjust="spacingAndGlyphs">FLOOR COATINGS</text>
    <g class="contact-row" transform="translate(0,214)">
      <use href="#phone-icon"/>
      <text class="contact-line" x="58" y="0" font-size="58" textLength="360" lengthAdjust="spacingAndGlyphs">555-014-2870</text>
      <use href="#laptop-icon" x="440"/>
      <text class="contact-line" x="505" y="0" font-size="58" textLength="550" lengthAdjust="spacingAndGlyphs">www.granitewellfloors.com</text>
    </g>
  </g>
</svg>
</body>
</html>
```